we need a business card in yellow, green and black with rounded edges. We are in the Construction and Engineering business. I need the below info included:

Neil Barton
Summitrow Engineering & Construction, Inc.
4158 Harbor Vale Drive,
Santa Ana, Ca 92705
714-555-0147 Office
714-555-0192 Cell
714-555-0163 Fax
nb@summitrowec.com

thanks for your help!

```html
<!DOCTYPE html>
<html lang="en">
<head>
<meta charset="utf-8">
<title>Neil Barton – Business Card</title>
<link rel="stylesheet" href="https://fonts.googleapis.com/css2?family=Saira+Condensed:wght@300;400&family=Lato:wght@400&display=swap">
<style>
  :root {
    --page-bg: #e9e7e3;
    --card-center: #4a4a4a;
    --card-mid: #262626;
    --card-edge: #111111;
    --ink-light: #ffffff;
    --ink-soft: #e6e6e6;
    --accent-yellow: #f5c518;
    --accent-green: #5fa83a;
    --icon-glyph: #1a1a1a;
  }
  * { margin: 0; padding: 0; box-sizing: border-box; }
  html, body {
    width: 1200px;
    height: 1000px;
    overflow: hidden;
    background: var(--page-bg);
  }
  .stage {
    position: relative;
    width: 1200px;
    height: 1000px;
  }
  .business-card {
    position: absolute;
    left: 180px;
    top: 248px;
    width: 840px;
    height: 504px;
    border-radius: 46px;
    background: radial-gradient(ellipse 60% 65% at 50% 50%, var(--card-center) 0%, var(--card-mid) 55%, var(--card-edge) 100%);
    box-shadow: 0 14px 34px rgba(0, 0, 0, 0.35);
    color: var(--ink-light);
  }
  .card-name {
    position: absolute;
    left: 85px;
    top: 84px;
    font-family: "Saira Condensed", sans-serif;
    font-weight: 400;
    font-size: 74px;
    line-height: 1;
    letter-spacing: 0.01em;
    color: var(--ink-light);
  }
  .card-company {
    position: absolute;
    left: 87px;
    top: 186px;
    font-family: "Saira Condensed", sans-serif;
    font-weight: 300;
    font-size: 18px;
    line-height: 1;
    letter-spacing: 0.2em;
    text-transform: uppercase;
    color: var(--accent-yellow);
    white-space: nowrap;
  }
  .contact-list {
    position: absolute;
    left: 64px;
    top: 278px;
    list-style: none;
  }
  .contact-item {
    display: flex;
    align-items: center;
    height: 36px;
    margin-bottom: 26px;
    font-family: "Lato", sans-serif;
    font-size: 18px;
    line-height: 1;
    color: var(--ink-soft);
    white-space: nowrap;
  }
  .contact-icon {
    width: 40px;
    height: 40px;
    margin-right: 12px;
    flex: none;
  }
  .icon-fill { fill: var(--accent-green); }
  .icon-glyph { fill: var(--icon-glyph); }
  .divider { margin: 0 8px; color: var(--accent-yellow); }
</style>
</head>
<body>
<main class="stage">
  <section class="business-card" aria-label="Business card of Neil Barton">
    <h1 class="card-name">Neil Barton</h1>
    <p class="card-company">Summitrow Engineering &amp; Construction, Inc.</p>
    <ul class="contact-list">
      <li class="contact-item">
        <svg class="contact-icon" viewBox="0 0 40 40" aria-hidden="true">
          <path class="icon-fill" d="M20 6c-5.2 0-9 3.9-9 8.9 0 6.4 9 16.6 9 16.6s9-10.2 9-16.6C29 9.9 25.2 6 20 6z"/>
          <circle cx="20" cy="15" r="3.4" fill="#262626"/>
        </svg>
        <span>4158 Harbor Vale Drive, Santa Ana, Ca 92705</span>
      </li>
      <li class="contact-item">
        <svg class="contact-icon" viewBox="0 0 40 40" aria-hidden="true">
          <circle class="icon-fill" cx="20" cy="20" r="19"/>
          <path class="icon-glyph" d="M10 16c0-2.5 4.5-4.5 10-4.5s10 2 10 4.5v1.6h-4.6v-2.2c-1.6-.6-3.4-.9-5.4-.9s-3.8.3-5.4.9v2.2H10z"/>
          <rect class="icon-glyph" x="12.5" y="19" width="15" height="9.5" rx="1.5"/>
          <circle class="icon-fill" cx="20" cy="23.7" r="2.4"/>
        </svg>
        <span>Office: 714-555-0147</span><span class="divider">|</span><span>Cell: 714-555-0192</span><span class="divider">|</span><span>Fax: 714-555-0163</span>
      </li>
      <li class="contact-item">
        <svg class="contact-icon" viewBox="0 0 40 40" aria-hidden="true">
          <circle class="icon-fill" cx="20" cy="20" r="19"/>
          <rect class="icon-glyph" x="10.5" y="13" width="19" height="14" rx="1"/>
          <path d="M11 14l9 7.5 9-7.5M11 26.5l6.5-6M29 26.5l-6.5-6" stroke="#5fa83a" stroke-width="1.4" fill="none"/>
        </svg>
        <span>nb@summitrowec.com</span>
      </li>
    </ul>
  </section>
</main>
</body>
</html>
```